Coffee Shop needs a fresh new menu

Hi,
I would like a new menu to be designed for our coffee shop.
We display our menu on a television screen, so would need it in a file that would allow us to continue to do so -- I have attached a photo so that you can see our current design, and how it is displayed.

I'd like something that is easy to read, if the design could have a "hipster" feel to it -- we are located at a hospital and University.

I have attached a Word file with what we would like on the menu.

Feel free to contact me if you have any questions.

Thanks,
Tam

Just A4 size will be fine, and no need to include menu 1 and menu 2 - I just put them in as an example of what we already have -- they are our printed menu's. Thanks

Hospital

```html
<!DOCTYPE html>
<html lang="en">
<head>
<meta charset="utf-8">
<title>Elm Coffee Shop Menu</title>
<link href="https://fonts.googleapis.com/css2?family=Anton&family=Courgette&family=Oswald:wght@400;500&display=swap" rel="stylesheet">
<style>
  :root {
    --backdrop: #cfcfcf;
    --wood-dark: #1c1512;
    --wood-mid: #3a2a22;
    --wood-light: #5a4034;
    --cup-white: #e9e6e2;
    --red-deep: #6e0a0f;
    --red-main: #9e141b;
    --red-glow: #cf3a43;
    --ink-light: #ffffff;
    --ink-soft: rgba(255,255,255,0.82);
    --rule: rgba(255,255,255,0.45);
  }
  * { box-sizing: border-box; margin: 0; padding: 0; }
  html, body { width: 1200px; height: 1000px; overflow: hidden; }
  body { background: var(--backdrop); position: relative; }

  .menu-sheet {
    position: absolute; left: 268px; top: 30px;
    width: 664px; height: 940px; overflow: hidden;
    background: var(--red-main);
    box-shadow: 0 6px 18px rgba(0,0,0,0.25);
    color: var(--ink-light);
    font-family: "Oswald", sans-serif;
  }

  .hero-photo {
    position: absolute; left: 0; top: 0; width: 664px; height: 350px;
    background:
      radial-gradient(ellipse 190px 150px at 470px 270px, var(--cup-white) 0%, #bdb6ae 45%, rgba(90,64,52,0) 100%),
      radial-gradient(ellipse 120px 80px at 250px 320px, #6b4226 0%, rgba(60,40,30,0) 100%),
      linear-gradient(100deg, var(--wood-mid) 0%, var(--wood-dark) 45%, var(--wood-light) 70%, var(--wood-dark) 100%);
  }
  .brand-strip {
    position: absolute; left: 40px; top: 0; width: 150px; height: 290px;
    background: rgba(70,45,35,0.75);
  }
  .brand {
    position: absolute; left: 40px; top: 80px; width: 150px;
    text-align: center; color: var(--ink-light);
    font-family: "Oswald", sans-serif; font-weight: 500;
  }
  .brand-mark {
    display: block; width: 18px; height: 18px; border-radius: 50%;
    background: var(--ink-light); margin: 0 auto 10px;
  }
  .brand-name { display: block; font-size: 44px; line-height: 1; letter-spacing: 2px; }
  .brand-sub { display: block; font-size: 20px; line-height: 1.05; margin-top: 8px; letter-spacing: 1px; }

  .menu-title {
    position: absolute; left: 38px; top: 272px;
    font-family: "Anton", sans-serif; font-size: 64px; letter-spacing: 1px;
    line-height: 1; color: var(--ink-light);
  }

  .menu-body {
    position: absolute; left: 0; top: 350px; width: 664px; height: 590px;
    background:
      radial-gradient(ellipse 260px 200px at 200px 160px, var(--red-glow) 0%, rgba(207,58,67,0) 100%),
      radial-gradient(ellipse 300px 240px at 470px 300px, #b92530 0%, rgba(185,37,48,0) 100%),
      linear-gradient(180deg, var(--red-main) 0%, var(--red-deep) 100%);
  }

  .menu-section { position: absolute; }
  .section-title {
    font-family: "Courgette", cursive; font-size: 21px; font-weight: 400;
    line-height: 26px; margin-bottom: 4px; color: var(--ink-light);
  }
  .item-list { list-style: none; }
  .item {
    display: grid; font-size: 12.5px; line-height: 15px;
    text-transform: uppercase; letter-spacing: 0.4px;
  }
  .item-pair { grid-template-columns: 1fr 60px; }
  .item-trio { grid-template-columns: 1fr 66px 66px; }
  .price { text-align: right; }
  .list-gap { height: 8px; }
  .section-rule {
    position: absolute; height: 1px; background: var(--rule);
  }

  .coffee { left: 34px; top: 14px; width: 300px; }
  .hot-food { left: 34px; top: 250px; width: 270px; }
  .something-light { left: 370px; top: 70px; width: 260px; }
  .breakfast { left: 370px; top: 270px; width: 260px; }
  .extras { left: 236px; top: 470px; width: 300px; }
  .extras-note {
    font-size: 9.5px; line-height: 12px; color: var(--ink-soft); margin-top: 4px;
    display: grid; grid-template-columns: 1fr 60px;
  }
</style>
</head>
<body>
  <main class="menu-sheet">
    <div class="hero-photo" role="img" aria-label="Photo of a steaming white coffee cup on a saucer with roasted coffee beans on a dark wooden table"></div>
    <div class="brand-strip"></div>
    <div class="brand">
      <span class="brand-mark"></span>
      <span class="brand-name">ELM</span>
      <span class="brand-sub">COFFEE<br>SHOP</span>
    </div>
    <h1 class="menu-title">MENU</h1>

    <section class="menu-body">
      <div class="menu-section coffee">
        <h2 class="section-title">Coffee</h2>
        <ul class="item-list">
          <li class="item item-trio"><span>Latte</span><span class="price">Small $4.00</span><span class="price">Large $4.50</span></li>
          <li class="item item-trio"><span>Cappuccino</span><span class="price">Small $4.00</span><span class="price">Large $4.50</span></li>
          <li class="item item-trio"><span>Flat White</span><span class="price">Small $4.00</span><span class="price">Large $4.50</span></li>
          <li class="item item-trio"><span>Long Black</span><span class="price">Small $4.00</span><span class="price">Large $4.50</span></li>
          <li class="item item-trio"><span>Hot Chocolate</span><span class="price">Small $4.00</span><span class="price">Large $4.50</span></li>
          <li class="item item-trio"><span>Chai Latte</span><span class="price">Small $4.50</span><span class="price">Large $5.00</span></li>
          <li class="item item-trio"><span>Mocha</span><span class="price">Small $4.50</span><span class="price">Large $5.00</span></li>
          <li class="item item-trio"><span>Dirty Chai</span><span class="price">Small $5.00</span><span class="price">Large $5.50</span></li>
          <li class="list-gap"></li>
          <li class="item item-pair"><span>Espresso</span><span class="price">$3.50</span></li>
          <li class="item item-pair"><span>Short Macchiato</span><span class="price">$3.50</span></li>
          <li class="item item-pair"><span>Piccolo</span><span class="price">$4.00</span></li>
          <li class="item item-pair"><span>Long Macchiato</span><span class="price">$4.00</span></li>
        </ul>
      </div>
      <div class="section-rule" style="left:30px; top:240px; width:290px;"></div>

      <div class="menu-section hot-food">
        <h2 class="section-title">Hot Food and Sandwiches:</h2>
        <ul class="item-list">
          <li class="item item-pair"><span>Premade Sandwiches</span><span class="price">$6.50</span></li>
          <li class="item item-pair"><span>Premade Focaccias</span><span class="price">$7.50</span></li>
          <li class="item item-pair"><span>Wraps</span><span class="price">$7.50</span></li>
          <li class="item item-pair"><span>Vegetarian Salad</span><span class="price">$7.50</span></li>
          <li class="item item-pair"><span>Meat/Seafood Salad</span><span class="price">$9.50</span></li>
          <li class="item item-pair"><span>Hot Chips</span><span class="price">$4.00</span></li>
          <li class="item item-pair"><span>Dim Sim</span><span class="price">$1.50</span></li>
          <li class="item item-pair"><span>Potato Cake</span><span class="price">$1.50</span></li>
          <li class="item item-pair"><span>Plain Hamburger</span><span class="price">$7.50</span></li>
          <li class="item item-pair"><span>Hamburger with Lot</span><span class="price">$9.00</span></li>
          <li class="item item-pair"><span>Chicken Schnitzel Burger</span><span class="price">$8.50</span></li>
        </ul>
      </div>

      <div class="menu-section something-light">
        <h2 class="section-title">Something Light:</h2>
        <ul class="item-list">
          <li class="item item-pair"><span>Mixed Yoghurts</span><span class="price">$6.50</span></li>
          <li class="item item-pair"><span>Chia Pudding</span><span class="price">$6.50</span></li>
          <li class="item item-pair"><span>Fruit Salad</span><span class="price">$6.50</span></li>
          <li class="item item-pair"><span>Bircher Muesli</span><span class="price">$6.50</span></li>
          <li class="item item-pair"><span>Protein Balls</span><span class="price">$4.00</span></li>
          <li class="item item-pair"><span>Banana Bread</span><span class="price">$4.50</span></li>
          <li class="item item-pair"><span>Muffins</span><span class="price">$4.50</span></li>
          <li class="item item-pair"><span>Slices</span><span class="price">$4.00</span></li>
        </ul>
      </div>
      <div class="section-rule" style="left:360px; top:260px; width:280px;"></div>

      <div class="menu-section breakfast">
        <h2 class="section-title">Breakfast Items:</h2>
        <ul class="item-list">
          <li class="item item-pair"><span>Bacon, Egg and Cheese Roll</span><span class="price">$6.00</span></li>
          <li class="item item-pair"><span>Ham and Cheese Toastie</span><span class="price">$5.00</span></li>
          <li class="item item-pair"><span>Cheese and Tomato Toastie</span><span class="price">$5.00</span></li>
          <li class="item item-pair"><span>Ham and Cheese Croissant</span><span class="price">$5.50</span></li>
          <li class="item item-pair"><span>Cheese and Tomato Croissant</span><span class="price">$5.50</span></li>
          <li class="item item-pair"><span>Plain Croissant</span><span class="price">$3.50</span></li>
          <li class="item item-pair"><span>Hashbrown</span><span class="price">$2.00</span></li>
          <li class="item item-pair"><span>2 Piece Toast</span><span class="price">$3.00</span></li>
          <li class="item item-pair"><span>2 Piece Raisin Toast</span><span class="price">$3.00</span></li>
        </ul>
      </div>
      <div class="section-rule" style="left:230px; top:462px; width:410px;"></div>

      <div class="menu-section extras">
        <h2 class="section-title">Extras</h2>
        <ul class="item-list">
          <li class="item item-pair"><span>Soymilk/Lactose Free Milk/Syrups/Extra Shot/Decaf</span><span class="price">$0.50</span></li>
        </ul>
        <p class="extras-note"><span>Tea, iced drinks, juices and cold cans also available at the counter, please ask.</span><span class="price">$4.00</span></p>
        <p class="extras-note"><span>Gluten free bread, dairy free milk and extra sauce on request.</span><span></span></p>
      </div>
    </section>
  </main>
</body>
</html>
```